Banner Ad Designs for tick and flea products

We sell tick and flea products online and want some great banner designs for our online website to promote our tick and flea products.

The ads must be made up in both Flash and HTML5
Ads can be formatted as .JPEG or .GIF files.

Please see the following url for creative requirements
http://help.bannerquay.com/creative-requirements/

Creative licence no limits to your imagination!

Ads must be created in the following sizes:

- Banner – 468×60
- Square – 250×250
- Small Square – 200×200
- Leaderboard – 728×90
- Medium Rectangle – 300×250
- Chatterbox – 100×72

please view our website at www.harbourlanepawstore.com.au or .com to get a feel for our website.

The aim is to attract customers who want to save on tick and flea purchases for their pets (dogs and cats)

Target Market(s)

Anyone who owns a dog or cat

Industry/Entity Type

Online

Font styles to use
Sans Serif
Other font styles liked:
• creative licence on font styles

Requirements
Must have
• Must have a strong urge to entice customers to click through.

Images wording and text etc use creative lic
Nice to have
• Strong appeal to dog and cat owners and how they can save on flea and tick essentials.
Keep it simple but effective.
Be fun and playful and inviting.
Should not have
• Please do not use words like cheap - cheapest

Strobing & Flashing - Strobing, flashing backgrounds, or otherwise distracting ads are not allowed. Do not attempt to overtly distract the user from page content.

```html
<!DOCTYPE html>
<html lang="en">
<head>
<meta charset="utf-8">
<title>Harbour Lane Paw Store – Leaderboard Frames</title>
<link rel="stylesheet" href="https://fonts.googleapis.com/css2?family=Arimo:wght@400;700&display=swap">
<style>
  :root {
    --page-bg: #ffffff;
    --label-blue: #1f6fbf;
    --frame-green: #0b9a22;
    --panel-light: #f4f4f4;
    --panel-shade: #d6d6d6;
    --accent-red: #d4123f;
    --pink: #ff00c8;
    --pink-light: #ff5ae0;
    --navy: #0b2f66;
    --edge-blue: #2f86e8;
    --headline-purple: #5b1d4c;
    --headline-white: #ffffff;
    --button-lime: #a7dc1c;
    --button-lime-light: #d8f56a;
    --button-lime-dark: #5f9a0a;
    --button-text: #2f4a08;
    --button-icon: #3c6408;
    --logo-ink: #2b2b2b;
    --logo-dot: #c2186b;
    --photo-tan: #d19a52;
    --photo-grey: #8d8478;
  }
  * { box-sizing: border-box; margin: 0; padding: 0; }
  html, body {
    width: 1200px; height: 988px; overflow: hidden;
    background: var(--page-bg);
    font-family: "Arimo", Arial, sans-serif;
  }
  .sheet { position: relative; width: 1200px; height: 988px; }

  .frame-row { position: absolute; left: 0; width: 1200px; height: 127px; }
  .frame-row--a { top: 217px; }
  .frame-row--b { top: 360px; }
  .frame-row--c { top: 501px; }

  .frame-label {
    position: absolute; left: 17px; top: 0; height: 127px;
    display: flex; align-items: center;
    color: var(--label-blue); font-size: 24px; font-weight: 400; letter-spacing: 0.5px;
  }

  .banner-slot { position: absolute; left: 145px; top: 0; width: 1028px; height: 127px; }
  .banner {
    position: relative; width: 728px; height: 90px;
    transform: scale(1.4121); transform-origin: 0 0;
    background: var(--frame-green);
    outline: 1px solid #1b1b1b;
    overflow: hidden;
  }
  .banner-shapes { position: absolute; inset: 0; width: 728px; height: 90px; }

  .brand {
    position: absolute; left: 14px; top: 30px;
    display: flex; align-items: center; gap: 5px;
  }
  .brand-dot { width: 14px; height: 14px; border-radius: 50%; background: var(--logo-dot); }
  .brand-name {
    color: var(--logo-ink); font-size: 13px; font-weight: 700; line-height: 15px; width: 110px;
  }

  .pet-photo {
    position: absolute; left: 146px; top: 6px; width: 130px; height: 80px;
    background: linear-gradient(90deg, var(--photo-tan) 0%, #e2b573 45%, var(--photo-grey) 75%, rgba(141,132,120,0) 100%);
    border-radius: 4px;
  }

  .headline {
    position: absolute; left: 292px; top: 0; width: 246px; height: 90px;
    display: flex; align-items: center; justify-content: center; text-align: center;
    font-weight: 700; font-size: 21px; line-height: 21px;
  }
  .headline--dark { color: var(--headline-purple); text-shadow: 1px 1px 0 rgba(255,255,255,0.75); }
  .headline--light { color: var(--headline-white); font-size: 23px; line-height: 23px; text-shadow: 1px 2px 1px rgba(80,0,60,0.8); }
  .headline--dark.headline--three { font-size: 20px; line-height: 20px; }

  .order-button {
    position: absolute; left: 568px; top: 23px; width: 149px; height: 43px;
    border-radius: 7px;
    background: linear-gradient(180deg, var(--button-lime-light) 0%, var(--button-lime) 50%, var(--button-lime-dark) 100%);
    box-shadow: 0 2px 3px rgba(0,0,0,0.45), inset 0 1px 0 rgba(255,255,255,0.6);
    display: flex; align-items: center; padding-left: 9px; gap: 8px;
    color: var(--button-text); font-weight: 700; font-size: 14px; text-decoration: none;
  }
  .order-button-icon {
    width: 27px; height: 25px; border-radius: 3px; background: var(--button-icon);
    display: flex; align-items: center; justify-content: center;
  }
</style>
</head>
<body>
<main class="sheet">

  <section class="frame-row frame-row--a">
    <div class="frame-label">FRAME A</div>
    <div class="banner-slot">
      <div class="banner">
        <svg class="banner-shapes" viewBox="0 0 728 90" aria-hidden="true">
          <defs>
            <linearGradient id="panelA" x1="0" y1="0" x2="1" y2="0"><stop offset="0" stop-color="#d6d6d6"/><stop offset="0.25" stop-color="#f4f4f4"/><stop offset="1" stop-color="#ffffff"/></linearGradient>
            <linearGradient id="pinkA" x1="0" y1="0" x2="1" y2="0"><stop offset="0" stop-color="#ff6be4"/><stop offset="0.3" stop-color="#ff00c8"/><stop offset="1" stop-color="#ff00c8"/></linearGradient>
          </defs>
          <path d="M5,5 H262 Q286,45 262,85 H5 Z" fill="url(#panelA)"/>
          <path d="M258,0 H278 Q304,45 278,90 H258 Q284,45 258,0 Z" fill="#d4123f"/>
          <path d="M276,0 H560 V90 H276 Q302,45 276,0 Z" fill="url(#pinkA)"/>
          <path d="M550,0 H728 V90 H550 Q526,45 550,0 Z" fill="#0b2f66"/>
          <path d="M550,0 Q526,45 550,90" fill="none" stroke="#2f86e8" stroke-width="5"/>
        </svg>
        <div class="brand"><span class="brand-dot"></span><span class="brand-name">Harbour Lane Paw Store</span></div>
        <div class="pet-photo" role="img" aria-label="Photo of a golden dog lying beside a tabby cat"></div>
        <p class="headline headline--dark">Available The Best<br>Quality Pet Supplies</p>
        <a class="order-button" href="#">ORDER NOW
          <span class="order-button-icon"><svg width="10" height="12" viewBox="0 0 10 12"><path d="M1,1 L9,6 L1,11 Z" fill="#ffffff"/></svg></span>
        </a>
      </div>
    </div>
  </section>

  <section class="frame-row frame-row--b">
    <div class="frame-label">FRAME B</div>
    <div class="banner-slot">
      <div class="banner">
        <svg class="banner-shapes" viewBox="0 0 728 90" aria-hidden="true">
          <defs>
            <linearGradient id="panelB" x1="0" y1="0" x2="1" y2="0"><stop offset="0" stop-color="#d6d6d6"/><stop offset="0.25" stop-color="#f4f4f4"/><stop offset="1" stop-color="#ffffff"/></linearGradient>
            <linearGradient id="pinkB" x1="0" y1="0" x2="1" y2="0"><stop offset="0" stop-color="#ff6be4"/><stop offset="0.3" stop-color="#ff00c8"/><stop offset="1" stop-color="#ff00c8"/></linearGradient>
          </defs>
          <path d="M5,5 H262 Q286,45 262,85 H5 Z" fill="url(#panelB)"/>
          <path d="M258,0 H278 Q304,45 278,90 H258 Q284,45 258,0 Z" fill="#d4123f"/>
          <path d="M276,0 H560 V90 H276 Q302,45 276,0 Z" fill="url(#pinkB)"/>
          <path d="M550,0 H728 V90 H550 Q526,45 550,0 Z" fill="#0b2f66"/>
          <path d="M550,0 Q526,45 550,90" fill="none" stroke="#2f86e8" stroke-width="5"/>
        </svg>
        <div class="brand"><span class="brand-dot"></span><span class="brand-name">Harbour Lane Paw Store</span></div>
        <div class="pet-photo" role="img" aria-label="Photo of a golden dog lying beside a tabby cat"></div>
        <p class="headline headline--light">From Fleas,<br>Heartworm,<br>and Worms</p>
        <a class="order-button" href="#">ORDER NOW
          <span class="order-button-icon"><svg width="10" height="12" viewBox="0 0 10 12"><path d="M1,1 L9,6 L1,11 Z" fill="#ffffff"/></svg></span>
        </a>
      </div>
    </div>
  </section>

  <section class="frame-row frame-row--c">
    <div class="frame-label">FRAME C</div>
    <div class="banner-slot">
      <div class="banner">
        <svg class="banner-shapes" viewBox="0 0 728 90" aria-hidden="true">
          <defs>
            <linearGradient id="panelC" x1="0" y1="0" x2="1" y2="0"><stop offset="0" stop-color="#d6d6d6"/><stop offset="0.25" stop-color="#f4f4f4"/><stop offset="1" stop-color="#ffffff"/></linearGradient>
            <linearGradient id="pinkC" x1="0" y1="0" x2="1" y2="0"><stop offset="0" stop-color="#ff6be4"/><stop offset="0.3" stop-color="#ff00c8"/><stop offset="1" stop-color="#ff00c8"/></linearGradient>
          </defs>
          <path d="M5,5 H262 Q286,45 262,85 H5 Z" fill="url(#panelC)"/>
          <path d="M258,0 H278 Q304,45 278,90 H258 Q284,45 258,0 Z" fill="#d4123f"/>
          <path d="M276,0 H560 V90 H276 Q302,45 276,0 Z" fill="url(#pinkC)"/>
          <path d="M550,0 H728 V90 H550 Q526,45 550,0 Z" fill="#0b2f66"/>
          <path d="M550,0 Q526,45 550,90" fill="none" stroke="#2f86e8" stroke-width="5"/>
        </svg>
        <div class="brand"><span class="brand-dot"></span><span class="brand-name">Harbour Lane Paw Store</span></div>
        <div class="pet-photo" role="img" aria-label="Photo of a golden dog lying beside a tabby cat"></div>
        <p class="headline headline--dark headline--three">Your Pets Deserves<br>The Best The<br>World Has To Offer</p>
        <a class="order-button" href="#">ORDER NOW
          <span class="order-button-icon"><svg width="10" height="12" viewBox="0 0 10 12"><path d="M1,1 L9,6 L1,11 Z" fill="#ffffff"/></svg></span>
        </a>
      </div>
    </div>
  </section>

</main>
</body>
</html>
```